maple crest homeworks KOVA

Looking for business card design that represents our company. we are maple crest homeworks and we dedicate our skills of home energy efficiency to our customer by providing energy solution to their energy problems.
HVAC
SOLAR
INSULLATION
LIGHTING
DUCT TESTING
KOVA RATING.

```html
<!DOCTYPE html>
<html lang="en">
<head>
<meta charset="utf-8">
<title>Maple Crest Homeworks — Business Card</title>
<link href="https://fonts.googleapis.com/css2?family=Roboto:wght@300;400;500&family=Roboto+Condensed:wght@700&display=swap" rel="stylesheet">
<style>
  :root {
    --page: #e9e7e3;
    --card-white: #f7f7f5;
    --card-black: #050505;
    --ink: #6b6b6b;
    --ink-light: #ffffff;
    --brand-blue: #1ba8e0;
    --brand-green: #8cc63f;
    --panel-dark: #1c1c1c;
  }
  * { margin: 0; padding: 0; box-sizing: border-box; }
  html, body { width: 1200px; height: 950px; overflow: hidden; }
  body {
    background: var(--page);
    font-family: "Roboto", Arial, sans-serif;
    display: flex;
    flex-direction: column;
    align-items: center;
    justify-content: center;
    gap: 70px;
  }
  .card {
    position: relative;
    width: 700px;
    height: 400px;
    border-radius: 26px;
    overflow: hidden;
  }

  /* Front */
  .card-front { background: var(--card-white); border: 1px solid #d8d8d4; }
  .brand-panel {
    position: absolute;
    left: 44px; top: 44px;
    width: 250px; height: 92px;
    background: var(--panel-dark);
    border: 3px solid var(--brand-green);
    border-radius: 10px;
    display: flex; align-items: center; gap: 12px;
    padding: 0 16px;
  }
  .brand-dot {
    width: 26px; height: 26px; flex: none;
    border-radius: 50%;
    background: var(--brand-blue);
  }
  .brand-name {
    font-weight: 400;
    font-size: 19px;
    line-height: 1.15;
    color: var(--brand-green);
    text-transform: uppercase;
    letter-spacing: 1px;
  }
  .contact {
    position: absolute;
    left: 50px; top: 168px;
    font-size: 16px;
    line-height: 24px;
    font-weight: 300;
    color: var(--ink);
  }
  .contact .address { margin-bottom: 14px; }
  .person {
    position: absolute;
    right: 44px; top: 44px;
    text-align: right;
    font-family: "Roboto Condensed", Arial, sans-serif;
    font-weight: 700;
    line-height: 1.1;
  }
  .person-name { color: var(--brand-blue); font-size: 26px; }
  .person-role { color: var(--brand-green); font-size: 17px; }
  .web-pill {
    position: absolute;
    right: 44px; bottom: 74px;
    background: var(--panel-dark);
    border: 2px solid var(--brand-green);
    border-radius: 6px;
    color: var(--ink-light);
    font-size: 15px;
    padding: 7px 16px;
  }
  .rule {
    position: absolute;
    left: 0; right: 0; bottom: 52px;
    height: 2px;
    background: var(--brand-green);
  }

  /* Back */
  .card-back {
    background: var(--card-black);
    display: flex; flex-direction: column;
    align-items: center; justify-content: center;
    gap: 44px;
  }
  .back-brand {
    display: flex; align-items: center; gap: 20px;
  }
  .back-brand .brand-dot { width: 48px; height: 48px; }
  .back-brand .brand-name { font-size: 40px; letter-spacing: 2px; }
  .services {
    list-style: none;
    display: flex; gap: 10px;
    color: var(--ink-light);
    font-size: 17px;
  }
  .services li::before {
    content: "";
    display: inline-block;
    width: 6px; height: 6px;
    margin: 0 8px 3px 0;
    border-radius: 50%;
    background: var(--brand-blue);
  }
</style>
</head>
<body>
  <section class="card card-front" aria-label="Business card front">
    <div class="brand-panel">
      <span class="brand-dot"></span>
      <span class="brand-name">Maple Crest<br>Homeworks</span>
    </div>
    <div class="person">
      <div class="person-name">DANA WHITFIELD</div>
      <div class="person-role">CEO/FOUNDER</div>
    </div>
    <div class="contact">
      <p class="address">4120 Larchwood Drive<br>Bellmont, Oregon 97410</p>
      <p>P. 503 218 4471</p>
      <p>M. 503 902 6635</p>
      <p>F. 503 218 4480</p>
      <p>E. dana@maplecresthomeworks.com</p>
    </div>
    <div class="web-pill">www.maplecresthomeworks.com</div>
    <div class="rule"></div>
  </section>

  <section class="card card-back" aria-label="Business card back">
    <div class="back-brand">
      <span class="brand-dot"></span>
      <span class="brand-name">Maple Crest<br>Homeworks</span>
    </div>
    <ul class="services">
      <li>HVAC</li>
      <li>Solar</li>
      <li>Insulation</li>
      <li>Lighting</li>
      <li>Duct Testing</li>
      <li>KOVA Rating.</li>
    </ul>
  </section>
</body>
</html>
```